lunetra.com redesign

We are a successful web hosting company that has been around since 1999 with 10,000 customers managing 2,000 websites and 12,000 domain names. Our challenge - we are losing ground because our site is getting old, our pricing is not competitive and our feature set needs to change to match the new world of mobile centric everything. We want to reach out to all of the domain names that we don't host websites for. We believe that if we designed a new site that focuses on bringing home all of those externally hosted websites to our own web hosting company that we would have a solid future. We need to compete against mopwizzle.com, vantrimble.com, kerbloom.com, zinqhut.com, nolvark.com, brimfolk.com, quorvane.com, welbix.com and 100,000 others. We need to simplify our message with clean design, focused pages, easy decision making processes for the consumer. We use WHMCS for the background provisioning and billing so we can pretty much manage any kind of pricing model and discounted promotion packages.
I would prefer Twitter bootstrap CSS based responsive design.

Reason: I was away on vacation for 2 weeks - I just got back - I need time to fairly review all submissions - thank you for your patience. Dorian Fenwick Lunetra.com

Thanks to all who submitted sample designs - unfortunately most of them were nothing much more than already available templates with some of my current content and logo added to them. I will try to be more specific to reduce the number of choices. I need the template be fully compatible with WHMCS and Wordpress if you can't make it work with WHMCS directly. Another question I have to ask is -"exactly what am I getting for my $500.00 - is it just a PSD template or actual integration of that theme into WHMCS or Wordpress?"  I don't expect anyone to create new content for the site at that price. What do you charge if  you are able to create content or get directly involved in the site implementation of that template?

```html
<!DOCTYPE html>
<html lang="en">
<head>
<meta charset="utf-8">
<title>Lunetra.com – Domains, Websites &amp; Hosting</title>
<link href="https://fonts.googleapis.com/css2?family=Open+Sans:wght@300;400;600;700;800&display=swap" rel="stylesheet">
<style>
:root{
  --brand-blue:#2c6cc8;
  --brand-blue-dark:#1d56ad;
  --nav-blue:#3b7fd9;
  --deep-navy:#143571;
  --accent-green:#8cc63f;
  --accent-green-dark:#74ad2b;
  --accent-orange:#f08a1c;
  --ink:#333;
  --ink-soft:#666;
  --line:#cfd6e0;
  --white:#fff;
}
*{box-sizing:border-box;margin:0;padding:0}
html,body{width:763px;height:1200px;overflow:hidden}
body{position:relative;background:var(--white);font-family:"Open Sans",Arial,sans-serif;color:var(--ink)}

/* header */
.site-header{position:absolute;left:0;top:0;width:763px;height:122px;background:linear-gradient(180deg,#3a7ed8,var(--brand-blue))}
.brand{position:absolute;left:30px;top:18px;font-size:50px;font-weight:800;color:var(--white);letter-spacing:-1px;line-height:1}
.account-links{position:absolute;right:40px;top:10px;display:flex;gap:6px}
.account-links a{font-size:10px;color:var(--brand-blue);background:var(--white);padding:3px 8px;border-radius:2px;text-decoration:none}
.main-nav{position:absolute;left:76px;top:96px;width:611px;height:26px;background:var(--white);display:flex;align-items:stretch;border-radius:2px 2px 0 0}
.main-nav a{flex:1;font-size:12px;color:var(--brand-blue);text-decoration:none;display:flex;align-items:center;justify-content:center;border-right:1px solid #e2e7ee}
.main-nav a.home{flex:0 0 34px;background:var(--nav-blue)}

/* hero */
.hero{position:absolute;left:0;top:122px;width:763px;height:254px;overflow:hidden}
.hero-photo{position:absolute;inset:0;background:linear-gradient(180deg,#f4f4f2 0%,#e8e6e1 55%,#b98a5a 72%,#8e6038 100%)}
.hero-title{position:absolute;left:110px;top:22px;font-size:30px;font-weight:400;color:var(--accent-orange)}
.hero-sub{position:absolute;left:110px;top:66px;width:360px;font-size:18px;line-height:22px;color:#444}
.hero-ticks{position:absolute;left:110px;top:114px;font-size:12px;color:#444;display:flex;gap:10px}
.hero-ticks span::before{content:"\2714 ";color:var(--accent-orange)}
.cta-signup{position:absolute;left:240px;top:150px;width:140px;height:42px;background:var(--accent-green);border-radius:3px;color:var(--white);font-size:19px;display:flex;align-items:center;justify-content:center}
.hero-arrow{position:absolute;top:100px;width:20px;height:40px}
.hero-dots{position:absolute;left:344px;top:232px;display:flex;gap:6px}
.hero-dots i{width:9px;height:9px;border-radius:50%;background:#c9c9c9;display:block}
.hero-dots i.on{background:var(--nav-blue)}

/* features */
.section-title{position:absolute;left:0;width:763px;text-align:center;font-weight:300;color:var(--brand-blue)}
.feature-tabs{position:absolute;left:100px;top:424px;width:563px;height:48px;display:flex;gap:8px}
.feature-tabs div{flex:1;border:1px solid var(--line);font-size:12px;color:#555;text-align:center;display:flex;align-items:center;justify-content:center;line-height:15px;padding:0 6px}

/* domain search */
.search-lead{position:absolute;left:88px;top:516px}
.search-lead strong{display:block;font-size:15px;color:var(--accent-green-dark);font-weight:600}
.search-lead small{font-size:9px;color:var(--ink-soft)}
.search-www{position:absolute;left:272px;top:500px;font-size:12px;color:#777}
.search-field{position:absolute;left:268px;top:517px;width:290px;height:40px;border:1px solid #bbb;font-size:22px;color:#f5b26c;padding-left:12px;display:flex;align-items:center}
.search-btn{position:absolute;left:562px;top:517px;width:128px;height:40px;background:var(--accent-green);color:var(--white);font-size:22px;display:flex;align-items:center;justify-content:center}

/* blocks */
.block-title{position:absolute;left:85px;font-size:17px;font-weight:400;color:#333}
.block-note{position:absolute;left:85px;font-size:10px;color:var(--ink-soft)}
.btn-blue{position:absolute;background:var(--nav-blue);color:var(--white);display:flex;align-items:center;justify-content:center;border-radius:2px}

.plans{position:absolute;left:100px;top:656px;border-collapse:collapse;font-size:11px;color:#444}
.plans th{font-weight:600;font-size:10px;text-align:left;padding:0 0 4px}
.plans td{padding:2px 0;height:18px}
.plans .c1{width:88px}.plans .c2{width:92px}.plans .c3{width:100px}.plans .c4{width:104px}.plans .c5{width:80px}

/* services */
.service{position:absolute;top:842px;width:150px;text-align:center}
.service svg{display:block;margin:0 auto}
.service span{display:block;margin-top:12px;font-size:17px;color:#333}

.why-title{position:absolute;left:85px;top:942px;font-size:19px;font-weight:400;color:var(--brand-blue)}
.why-text{position:absolute;left:85px;top:970px;width:500px;font-size:9px;line-height:12px;color:var(--ink-soft)}

/* footer */
.site-footer{position:absolute;left:0;top:1010px;width:763px;height:120px;background:var(--brand-blue)}
.foot-col{position:absolute;top:10px;color:var(--white)}
.foot-col h4{font-size:12px;font-weight:700;margin-bottom:3px}
.foot-col li{list-style:none;font-size:9.5px;line-height:12px}
.signup-field{position:absolute;left:505px;top:34px;width:130px;height:18px;background:var(--white)}
.signup-btn{position:absolute;left:637px;top:34px;width:52px;height:18px;background:var(--accent-green);color:var(--white);font-size:9px;display:flex;align-items:center;justify-content:center}
.social{position:absolute;left:512px;top:62px;display:flex;gap:8px}
.social i{display:block;width:26px;height:26px;border-radius:50%;background:#5b9ae8;border:2px solid var(--white)}

.payments{position:absolute;left:0;top:1130px;width:763px;height:36px;display:flex;justify-content:center;align-items:center;gap:10px}
.payments i{display:block;width:40px;height:18px;background:#dfe4ea;border-radius:2px}
.copyright{position:absolute;left:0;top:1166px;width:763px;height:34px;background:var(--deep-navy);color:#cdd8ec;font-size:10px;display:flex;align-items:center;justify-content:center}
</style>
</head>
<body>

<header class="site-header">
  <div class="brand">lunetra</div>
  <div class="account-links"><a href="#">Register</a><a href="#">Log in</a></div>
  <nav class="main-nav">
    <a class="home" href="#" aria-label="Home">
      <svg width="14" height="13" viewBox="0 0 14 13"><path d="M7 0 L14 6 H12 V13 H8.5 V9 H5.5 V13 H2 V6 H0 Z" fill="#fff"/></svg>
    </a>
    <a href="#">Domain</a><a href="#">Website</a><a href="#">Hosting Centre</a><a href="#">Pricing</a><a href="#">Support</a><a href="#" style="border-right:0">Contact Us</a>
  </nav>
</header>

<section class="hero">
  <div class="hero-photo" role="img" aria-label="Bright room with a wooden floor and a person working on a laptop"></div>
  <h1 class="hero-title">Lunetra's e-Lite Package</h1>
  <p class="hero-sub">Everything you need for your Business to succeed online</p>
  <div class="hero-ticks"><span>Domain name</span><span>Hosting</span><span>Email</span><span>SiteBuilder</span><span>More</span></div>
  <div class="cta-signup">Sign Up Now</div>
  <svg class="hero-arrow" style="left:26px" viewBox="0 0 20 40"><path d="M16 2 L4 20 L16 38" stroke="#fff" stroke-width="3" fill="none"/></svg>
  <svg class="hero-arrow" style="left:717px" viewBox="0 0 20 40"><path d="M4 2 L16 20 L4 38" stroke="#fff" stroke-width="3" fill="none"/></svg>
  <div class="hero-dots"><i class="on"></i><i></i><i></i><i></i></div>
</section>

<h2 class="section-title" style="top:392px;font-size:20px">Build your Website &amp; achieve Success !</h2>
<div class="feature-tabs">
  <div>Free<br>Domain Name</div>
  <div>Build<br>a Website</div>
  <div>Attractive<br>Hosting Packages</div>
  <div>Search Engine<br>Optimizations Tools</div>
</div>

<div class="search-lead"><strong>Start Now !</strong><small>Find your Domain</small></div>
<div class="search-www">WWW.</div>
<div class="search-field">yourname.com</div>
<div class="search-btn">Search</div>

<h3 class="block-title" style="top:576px">Website Development</h3>
<p class="block-note" style="top:600px">PageForge Web builder, Email business bundle &amp; Custom design</p>
<div class="btn-blue" style="left:530px;top:582px;width:68px;height:26px;font-size:14px">Click</div>

<h3 class="block-title" style="top:630px">Hosting- Choose your Hosting Package</h3>
<table class="plans">
  <tr><th class="c1"></th><th class="c2">Storage</th><th class="c3">Domain Name</th><th class="c4">E-mail Account</th><th class="c5">Annual Price</th></tr>
  <tr><td>e-Lite</td><td>100 MB</td><td>Included</td><td>Unlimited</td><td>$ 90</td></tr>
  <tr><td>e-200</td><td>200 MB</td><td>Included</td><td>Unlimited</td><td>$ 149</td></tr>
  <tr><td>e-500</td><td>500 MB</td><td>Included</td><td>Unlimited</td><td>$ 249</td></tr>
  <tr><td>e-1000</td><td>1000 MB</td><td>Included</td><td>Unlimited</td><td>$ 549</td></tr>
</table>
<div class="btn-blue" style="left:575px;top:744px;width:92px;height:30px;font-size:15px">Choose</div>

<h2 class="section-title" style="top:800px;font-size:21px;color:#333">Get these Free Services with all Accounts</h2>

<div class="service" style="left:75px">
  <svg width="60" height="52" viewBox="0 0 60 52"><path d="M6 16 H46 M36 6 L48 16 L36 26" stroke="#333" stroke-width="4" fill="none"/><path d="M54 36 H14 M24 26 L12 36 L24 46" stroke="#333" stroke-width="4" fill="none"/></svg>
  <span>Easy Transfer</span>
</div>
<div class="service" style="left:228px">
  <svg width="64" height="52" viewBox="0 0 64 52"><rect x="4" y="3" width="56" height="36" rx="2" fill="#333"/><rect x="9" y="8" width="46" height="26" fill="#fff"/><rect x="26" y="39" width="12" height="7" fill="#333"/><rect x="18" y="46" width="28" height="4" fill="#333"/></svg>
  <span>Site Builder</span>
</div>
<div class="service" style="left:392px">
  <svg width="66" height="52" viewBox="0 0 66 52"><path d="M16 40 A12 12 0 0 1 16 16 A16 16 0 0 1 46 12 A13 13 0 0 1 50 40 Z" fill="#333"/><path d="M33 22 V46 M25 38 L33 46 L41 38" stroke="#fff" stroke-width="3" fill="none"/></svg>
  <span>Quickstaller</span>
</div>
<div class="service" style="left:545px">
  <svg width="60" height="52" viewBox="0 0 60 52"><path d="M4 24 L56 4 L46 48 L30 36 Z" fill="#333"/><path d="M30 36 L56 4 L22 30 L24 46 Z" fill="#555"/></svg>
  <span>Be Found</span>
</div>

<h3 class="why-title">Why Lunetra.com ?</h3>
<p class="why-text">As an DNRA-accredited registrar for more than 10 years, Lunetra is a leading provider of domain registration, website hosting, website design, and email hosting for small and medium-sized businesses.</p>
<div class="btn-blue" style="left:600px;top:964px;width:86px;height:24px;font-size:11px">Read More</div>

<footer class="site-footer">
  <div class="foot-col" style="left:85px">
    <h4>About Lunetra</h4>
    <ul><li>About Us</li><li>Domain</li><li>Website</li><li>Hosting Centre</li><li>Pricing</li><li>Support</li><li>Contact Us</li></ul>
  </div>
  <div class="foot-col" style="left:290px">
    <h4>Useful Links</h4>
    <ul><li>Terms of use</li><li>Dispute Policy</li><li>Privacy Policy</li><li>Help Center</li><li>FAQ</li></ul>
  </div>
  <div class="foot-col" style="left:505px">
    <ul><li>Sign up for special offers</li></ul>
  </div>
  <div class="signup-field"></div>
  <div class="signup-btn">Submit</div>
  <div class="social"><i></i><i></i><i></i><i></i></div>
</footer>

<div class="payments" aria-label="Accepted payment methods"><i></i><i></i><i></i><i></i><i></i><i></i></div>
<div class="copyright">Copyright © 2014 Lunetra.com . All Rights Reserved</div>

</body>
</html>
```